Computer consultant website

Plivet Software is a newly started computer consulting company. It's a small one-man company that provides mostly Android applications but also websites in collaboration with designers. I'm running this company on the side of full time university studies.

I'm in need of a website which will function as:
Primarily - I'll direct potential clients to the page so they can read about the company, what i offer and past work.
Secondarily - Making my company visible through the web and maybe getting new clients.

The final design should look modern, clean and professional.

Pages that will be in the final website are (Note that it's not the exact titles as the page will not be in english):
* About
* Services (what Plivet offers)
* Portfolio/work
* Short news (like Framolines "News and press")
* Contact.

Inspiration
http://www.framoline.example/design/87836
http://www.quarnbelt.example/
http://www.framoline.example/design/845881
http://www.framoline.example/design/1369424 - Lighter design, however a bit cluttered.

No programming code is needed delivered at all. Focus on designing rather then coding.

If you have any questions, do not hesitate to send me a message.

Target Market(s)

Non-technical entrepreneurs and small companies.

Industry/Entity Type

University

Requirements
Must have
• Must have my company logo (see attachment).

Must in any way use both colors from my logo.

A way to logically rearrange content to fit smaller screens. I will implement this design so that it can be pleasantly viewed on mobile devices. You don't necessarily need to provide exactly how the design would look on mobile devices.

I need the following types of page designs:
* Landing page
* Content page
* Portfolio/work (with accompanying inside/clicked) page

Landing/start page must in any way include at least the information:
* Shorter version of "About Plivet"
* At least 1 most recent portfolio/work entry
* At least 1 most recent news entry
* Services that Plivet offers.
Nice to have
• -
Should not have
• Testimonials or newsletter.

```html
<!DOCTYPE html>
<html lang="en">
<head>
<meta charset="utf-8">
<title>Plivet – About Us</title>
<link rel="stylesheet" href="https://fonts.googleapis.com/css2?family=Carlito:wght@400;700&display=swap">
<style>
  :root {
    --blue: #2779ec;
    --blue-dark: #1a63cf;
    --ink: #2e2e2e;
    --text: #4a4a4a;
    --muted: #8a8a8a;
    --canvas: #f3f3f3;
    --white: #ffffff;
    --rule: #e2e2e2;
    --dark: #2f2c2d;
    --footer: #1a1a1a;
  }
  * { margin: 0; padding: 0; box-sizing: border-box; }
  html, body { width: 1200px; height: 900px; overflow: hidden; }
  body { background: var(--canvas); font-family: "Carlito", "Calibri", sans-serif; color: var(--text); }
  .page { position: absolute; left: 246px; top: 4px; width: 708px; height: 892px; background: var(--white); }
  .abs { position: absolute; }

  /* header */
  .site-header { left: 0; top: 0; width: 708px; height: 61px; background: linear-gradient(#ffffff, #ececec); }
  .brand { left: 87px; top: 13px; display: flex; align-items: center; gap: 9px; }
  .brand-dot { width: 34px; height: 34px; border-radius: 50%; background: var(--blue); }
  .brand-name { font-size: 31px; font-weight: 700; color: #333; letter-spacing: 0.5px; }
  .main-nav { left: 289px; top: 0; height: 61px; display: flex; border-left: 1px solid var(--rule); }
  .main-nav a { position: relative; display: block; height: 61px; line-height: 61px; padding: 0 9px; font-size: 12px; color: #444; text-decoration: none; border-right: 1px solid var(--rule); }
  .main-nav a.is-active { background: linear-gradient(#3a8af5, var(--blue)); color: var(--white); }
  .main-nav a.is-active::after { content: ""; position: absolute; left: 50%; bottom: -5px; margin-left: -5px; border: 5px solid transparent; border-bottom: 0; border-top-color: var(--blue); }

  /* hero */
  .hero { left: 0; top: 61px; width: 708px; height: 181px; overflow: hidden; background: var(--white); }
  .hero-arc { left: 29px; top: 7px; }
  .hero-photo { left: 374px; top: 0; width: 266px; height: 181px; background: linear-gradient(90deg, rgba(255,255,255,0) 0%, #dbe6f0 25%, #c9d6e2 60%, rgba(255,255,255,0) 100%); }
  .hero-title { left: 93px; top: 58px; font-size: 28px; color: var(--ink); }
  .hero-title span { color: var(--blue); }
  .hero-lead { left: 93px; top: 89px; width: 230px; font-size: 13px; line-height: 15.5px; color: #555; }
  .btn-more { left: 252px; top: 133px; padding: 3px 8px; border-radius: 7px; background: var(--blue); color: var(--white); font-size: 11px; }
  .slide-arrow { top: 137px; width: 23px; height: 23px; }
  .slide-arrow.prev { left: 29px; }
  .slide-arrow.next { left: 654px; }

  /* feature band */
  .feature-band { left: 0; top: 242px; width: 708px; height: 64px; background: var(--blue); }
  .feature { top: 7px; width: 170px; color: var(--white); }
  .feature svg { position: absolute; left: -31px; top: 0; }
  .feature h3 { font-size: 14.5px; font-weight: 400; line-height: 17px; }
  .feature p { margin-top: 3px; font-size: 8.3px; font-weight: 700; line-height: 10.3px; }
  .feature-divider { top: 6px; width: 1px; height: 52px; background: rgba(0,0,0,0.15); }

  /* content */
  .about { left: 83px; top: 342px; width: 344px; }
  .about h1 { font-size: 17.5px; font-weight: 400; color: var(--ink); }
  .lede { margin-top: 7px; font-size: 7.6px; font-weight: 700; line-height: 10px; color: #222; }
  .body-copy { margin-top: 11px; font-size: 7.4px; line-height: 10.35px; color: #555; }
  .sidebar { left: 476px; top: 342px; width: 156px; }
  .sidebar h2 { font-size: 17.5px; font-weight: 400; color: var(--blue); }
  .sidebar h3 { margin-top: 24px; font-size: 14px; font-weight: 400; color: var(--blue); }
  .sidebar .lede { margin-top: 8px; }
  .service-list { list-style: none; margin-top: 8px; }
  .service-list li { position: relative; padding-left: 8px; font-size: 7.1px; line-height: 12.8px; color: #555; }
  .service-list li::before { content: ""; position: absolute; left: 0; top: 4.5px; width: 4px; height: 4px; border-radius: 50%; background: var(--blue); }
  .sidebar .small-copy { margin-top: 9px; font-size: 7.2px; line-height: 9.3px; color: #444; }

  /* showcase */
  .showcase { left: 0; top: 658px; width: 708px; height: 202px; background: var(--dark); border-top: 4px solid var(--blue); }
  .card { top: 27px; width: 157px; height: 145px; background: linear-gradient(#ffffff 70%, #e9e9e9); box-shadow: 0 6px 6px rgba(0,0,0,0.45); text-align: center; }
  .card h3 { margin: 9px 6px 0; padding-bottom: 3px; border-bottom: 1px solid var(--rule); font-size: 14px; font-weight: 400; color: var(--blue); }
  .card svg { display: block; margin: 6px auto 0; }
  .card p { margin: 4px 8px 0; font-size: 7.5px; line-height: 9.2px; color: #333; }

  /* footer */
  .site-footer { left: 0; top: 860px; width: 708px; height: 32px; background: var(--footer); font-size: 7.4px; color: #6a6a6a; }
  .copyright { left: 90px; top: 13px; }
  .footer-nav { right: 92px; top: 13px; display: flex; gap: 12px; }
  .footer-nav a { color: #6a6a6a; text-decoration: none; }
  .footer-nav a.is-active { color: var(--white); }
</style>
</head>
<body>
<div class="page">

  <header class="site-header abs">
    <div class="brand abs"><span class="brand-dot"></span><span class="brand-name">plivet</span></div>
    <nav class="main-nav abs">
      <a href="#">Home</a>
      <a href="#" class="is-active">About Us</a>
      <a href="#">Services</a>
      <a href="#">Portfolio</a>
      <a href="#">News</a>
      <a href="#">Contact Us</a>
    </nav>
  </header>

  <section class="hero abs">
    <svg class="hero-arc abs" width="360" height="260" viewBox="0 0 360 260" aria-hidden="true">
      <circle cx="185" cy="190" r="165" fill="none" stroke="#ececec" stroke-width="48"/>
    </svg>
    <div class="hero-photo abs" role="img" aria-label="Photo of two business people working at a laptop in a bright office"></div>
    <h2 class="hero-title abs">Lorem <span>ipsum dolor</span></h2>
    <p class="hero-lead abs">Sit amet, consectetur adipiscing elit. Nulla lobortis consequat mauris, eget eleifend</p>
    <span class="btn-more abs">Read more</span>
    <svg class="slide-arrow prev abs" viewBox="0 0 24 24" aria-label="Previous slide">
      <circle cx="12" cy="12" r="11" fill="#2a2a2a" stroke="var(--blue)" stroke-width="2"/>
      <path d="M14 7 L9 12 L14 17" fill="none" stroke="#fff" stroke-width="2.4"/>
    </svg>
    <svg class="slide-arrow next abs" viewBox="0 0 24 24" aria-label="Next slide">
      <circle cx="12" cy="12" r="11" fill="#2a2a2a" stroke="var(--blue)" stroke-width="2"/>
      <path d="M10 7 L15 12 L10 17" fill="none" stroke="#fff" stroke-width="2.4"/>
    </svg>
  </section>

  <section class="feature-band abs">
    <div class="feature abs" style="left:108px">
      <svg width="22" height="24" viewBox="0 0 22 24" aria-hidden="true">
        <circle cx="10" cy="10" r="9" fill="none" stroke="#111" stroke-width="2"/>
        <ellipse cx="10" cy="10" rx="4" ry="9" fill="none" stroke="#111" stroke-width="1.5"/>
        <path d="M1 10 H19 M3 5 H17 M3 15 H17" stroke="#111" stroke-width="1.3"/>
        <path d="M12 12 L21 16 L17 17 L19 22 L17 23 L15 18 L12 20 Z" fill="#111"/>
      </svg>
      <h3>Lorem ipsum dolor sit</h3>
      <p>Consectetur adipiscing elit. Nulla lobortis consequat mauris, eget eleifend nunc viverra viverra.</p>
    </div>
    <div class="feature-divider abs" style="left:262px"></div>
    <div class="feature abs" style="left:307px">
      <svg width="22" height="24" viewBox="0 0 22 24" aria-hidden="true">
        <path d="M11 2 A7 7 0 0 1 15 15 V18 H7 V15 A7 7 0 0 1 11 2 Z" fill="none" stroke="#111" stroke-width="2"/>
        <path d="M7 20 H15 M8 22.5 H14" stroke="#111" stroke-width="1.8"/>
      </svg>
      <h3>Lorem ipsum dolor sit</h3>
      <p>Consectetur adipiscing elit. Nulla lobortis consequat mauris, eget eleifend nunc viverra viverra.</p>
    </div>
    <div class="feature-divider abs" style="left:456px"></div>
    <div class="feature abs" style="left:506px">
      <svg width="24" height="26" viewBox="0 0 24 26" aria-hidden="true">
        <path d="M2 1 H12 L18 7 V24 H2 Z" fill="none" stroke="#111" stroke-width="2"/>
        <path d="M12 1 V7 H18" fill="none" stroke="#111" stroke-width="1.6"/>
        <path d="M18 14 V24 M13 19 H23" stroke="#111" stroke-width="3"/>
      </svg>
      <h3>Lorem ipsum dolor sit</h3>
      <p>Consectetur adipiscing elit. Nulla lobortis consequat mauris, eget eleifend nunc viverra viverra.</p>
    </div>
  </section>

  <main>
    <article class="about abs">
      <h1>About Us</h1>
      <p class="lede">Lorem ipsum dolor sit amet, consectetur adipiscing elit. Nulla lobortis consequat mauris, eget eleifend nunc viverra viverra. Ut ac risus odio. Aliquam pretium purus sed nulla feugiat blandit.</p>
      <p class="body-copy">Cras vel libero ut lacus eleifend tempor. Phasellus eleifend, magna non tincidunt accumsan, justo arcu cursus ipsum, non porttitor sapien quam vel magna. Maecenas elit nisl, molestie nec dapibus nec, aliquet a erat. Donec scelerisque lacus a libero suscipit auctor volutpat enim euismod. Mauris porta, lacus ut ullamcorper sodales, mauris tortor feugiat purus, nec aliquam neque purus ac metus. Nunc eleifend leo quis nisl hendrerit ultrices. Suspendisse quis feugiat elit. Fusce vitae dolor ac est tincidunt feugiat. Phasellus volutpat dui in sapien malesuada tempus placerat justo ultricies. Duis mollis ornare risus, ut consectetur mi tincidunt sit amet. Maecenas quis nibh ac orci tempus scelerisque ac et massa Maecenas quis nibh ac orci tempus scelerisque ac et massa. Cras vel libero ut lacus eleifend tempor. Phasellus eleifend, magna non tincidunt accumsan, justo arcu cursus ipsum, non porttitor sapien quam vel magna. Maecenas elit nisl, molestie nec dapibus nec, aliquet a erat. Donec scelerisque lacus a libero suscipit auctor volutpat enim euismod. Mauris porta, lacus ut ullamcorper sodales, mauris tortor feugiat purus, nec aliquam neque purus ac metus. Nunc eleifend leo quis nisl hendrerit ultrices. Suspendisse quis feugiat elit. Fusce vitae dolor ac est tincidunt feugiat. Phasellus volutpat dui in sapien malesuada tempus placerat justo ultricies. Duis mollis ornare risus, ut consectetur mi tincidunt sit amet. Maecenas quis nibh ac orci tempus scelerisque ac et massa Maecenas quis nibh ac orci tempus scelerisque ac et massa. Cras vel libero ut lacus eleifend tempor. Phasellus eleifend, magna non tincidunt accumsan, justo arcu cursus ipsum, non porttitor sapien quam vel magna. Maecenas elit nisl, molestie nec dapibus nec, aliquet a erat. Donec scelerisque lacus a libero suscipit auctor volutpat enim euismod. Mauris porta, lacus ut ullamcorper sodales, mauris tortor feugiat purus, nec aliquam neque purus ac metus. Nunc eleifend leo quis nisl hendrerit ultrices. Suspendisse quis feugiat elit. Fusce vitae dolor ac est tincidunt feugiat. Phasellus volutpat dui in sapien malesuada tempus placerat justo ultricies. Duis mollis ornare risus, ut consectetur mi tincidunt sit amet. Maecenas quis nibh ac orci tempus scelerisque ac et massa.</p>
    </article>

    <aside class="sidebar abs">
      <h2>Our Services</h2>
      <p class="lede">Lorem ipsum dolor sit amet, consectetur adipiscing elit. Nulla lobortis consequat mauris,</p>
      <ul class="service-list">
        <li>Cras vel libero ut lacus eleifend tempor.</li>
        <li>Phasellus eleifend, magna non tincidunt</li>
        <li>Accumsan, justo arcu cursus ipsum, non</li>
        <li>Porttitor sapien quam vel magna. Maecenas</li>
        <li>Elit nisl, molestie nec dapibus nec, aliquet a</li>
        <li>Erat. Donec scelerisque lacus a libero suscipit</li>
        <li>Auctor volutpat enim euismod. Mauris porta,</li>
      </ul>
      <h3>Lorem ipsum dolor sit</h3>
      <p class="small-copy">Nulla feugiat blandit. Cras vel libero ut lacus eleifend tempor. Phasellus eleifend, magna non tincidunt accumsan, justo arcu cursus ipsum, non porttitor sapien quam vel magna. Maecenas elit nisl, molestie nec dapibus nec, aliquet a erat. Donec scelerisque lacus a libero suscipit auctor volutpat enim euismod. Mauris porta, lacus ut ullamcorper sodales, mauris tortor feugiat purus, nec aliquam neque purus ac metus. Nunc eleifend leo quis nisl hendrerit ultrices. Suspendisse quis</p>
    </aside>
  </main>

  <section class="showcase abs">
    <div class="card abs" style="left:89px">
      <h3>Lorem ipsum dolor sit</h3>
      <svg width="48" height="46" viewBox="0 0 48 46" aria-hidden="true">
        <path d="M24 2 A21 19 0 1 1 14 38 L8 44 L10 35 A21 19 0 0 1 24 2 Z" fill="#f2f2f2" stroke="#9a9a9a" stroke-width="1.5"/>
        <path d="M24 9 V27" stroke="#333" stroke-width="4.5" stroke-linecap="round"/>
        <circle cx="24" cy="33" r="2.6" fill="#333"/>
      </svg>
      <p>Nulla feugiat blandit. Cras vel libero ut lacus eleifend tempor. Phasellus eleifend, magna non tincidunt accumsan, justo arcu cursus ipsum, non porttitor sapien quam vel magna. Maecenas elit nisl, molestie nec dapibus nec,</p>
    </div>
    <div class="card abs" style="left:275px">
      <h3>Lorem ipsum dolor sit</h3>
      <svg width="48" height="46" viewBox="0 0 48 48" aria-hidden="true">
        <g fill="#eeeeee" stroke="#b5b5b5" stroke-width="1.3">
          <path d="M21 2 H27 L28 8 L33 10 L38 6 L42 10 L38 15 L40 20 L46 21 V27 L40 28 L38 33 L42 38 L38 42 L33 38 L28 40 L27 46 H21 L20 40 L15 38 L10 42 L6 38 L10 33 L8 28 L2 27 V21 L8 20 L10 15 L6 10 L10 6 L15 10 L20 8 Z"/>
          <circle cx="24" cy="24" r="8" fill="#ffffff"/>
        </g>
      </svg>
      <p>Nulla feugiat blandit. Cras vel libero ut lacus eleifend tempor. Phasellus eleifend, magna non tincidunt accumsan, justo arcu cursus ipsum, non porttitor sapien quam vel magna. Maecenas elit nisl, molestie nec dapibus nec,</p>
    </div>
    <div class="card abs" style="left:461px">
      <h3>Lorem ipsum dolor sit</h3>
      <svg width="48" height="46" viewBox="0 0 48 46" aria-hidden="true">
        <path d="M8 3 H34 L40 9 V44 H8 Z" fill="#eeeeee" stroke="#c2c2c2" stroke-width="1.2"/>
        <path d="M32 3 L40 3 L40 12 Z" fill="var(--blue)"/>
        <path d="M22 16 V34 M13 25 H31" stroke="#111" stroke-width="5"/>
      </svg>
      <p>Nulla feugiat blandit. Cras vel libero ut lacus eleifend tempor. Phasellus eleifend, magna non tincidunt accumsan, justo arcu cursus ipsum, non porttitor sapien quam vel magna. Maecenas elit nisl, molestie nec dapibus nec,</p>
    </div>
  </section>

  <footer class="site-footer abs">
    <span class="copyright abs">Copyright information comes here</span>
    <nav class="footer-nav abs">
      <a href="#">Home</a>
      <a href="#" class="is-active">About Us</a>
      <a href="#">Services</a>
      <a href="#">Portfolio</a>
      <a href="#">News</a>
      <a href="#">Contact Us</a>
    </nav>
  </footer>

</div>
</body>
</html>
```